Powerpoint visual improvements

I need a cover page, and our beliefs page and differentiating factors page / graphic design for our presentation. For the cover page I would just like an attractive design that incorporate our architectural concept with columns and potentially our logo. For the beliefs page I just want a more attractive presentatoin of the concepts. For the differentiating factors page I want a graphic that captures the points about how we are different from competitors. I have used the attached content to date, but I think it can be improved. The text is included in the graphic and I would also like to make sure the firm logo is incorporated.

Target Market(s)

Individual and institutional investors.

Industry/Entity Type

Investment Advisory

Requirements
Must have
• Our corporate colors are generally RGB 145,148,149; 66,68,76; 0,0,153; and 0,63,127. Our logo is attached. Our primary font is Georgia. Our website is www.PelmarCW.com. The key pages are www.PelmarCW.com/beliefs and www.PelmarCW.com/value we are trying to capture in a presentation. We also need a new presentation cover. Use the website as a reference for the type of imagery we like.

```html
<!DOCTYPE html>
<html lang="en">
<head>
<meta charset="utf-8">
<title>The Pelmar Slide Ideas</title>
<link rel="stylesheet" href="https://fonts.googleapis.com/css2?family=Gelasio:wght@400;700&family=Open+Sans:wght@600&display=swap">
<style>
  :root{
    --board:#22304b;
    --paper:#f7f7f7;
    --ink:#1f2a44;
    --label:#2e3036;
    --grey:#919495;
    --charcoal:#42444c;
    --blue:#000099;
    --navy:#003f7f;
    --teal:#4aa3bb;
    --pink:#d9a7ab;
    --purple:#6b4fa0;
    --ring:#dedede;
  }
  html,body{margin:0;padding:0;width:1200px;height:1200px;overflow:hidden;background:var(--board);}
  .board{position:relative;width:1200px;height:1200px;}
  .board-title{position:absolute;top:40px;left:0;width:1200px;text-align:center;margin:0;
    font-family:"Open Sans",sans-serif;font-weight:600;font-size:25px;color:#fff;letter-spacing:-0.2px;}
  .slide{position:absolute;width:320px;height:180px;box-shadow:0 3px 8px rgba(0,0,0,.35);}
  .slide svg{display:block;width:320px;height:180px;}
  .sprites{position:absolute;width:0;height:0;overflow:hidden;}
  svg text{font-family:"Gelasio",Georgia,serif;}
  .ttl{font-size:12.5px;font-weight:700;fill:var(--ink);text-anchor:middle;}
  .lbl{font-size:5.6px;font-weight:700;fill:var(--label);text-anchor:middle;}
  .lbl-s{font-size:5.6px;font-weight:700;fill:var(--label);text-anchor:start;}
  .lbl-e{font-size:5.6px;font-weight:700;fill:var(--label);text-anchor:end;}
  .lbl-w{font-size:5.4px;font-weight:700;fill:#fff;text-anchor:middle;}
  .para{font-size:3.2px;text-anchor:middle;}
  .para-l{font-size:3.2px;text-anchor:start;fill:#7a7a7a;}
  .brand{font-size:8px;fill:var(--grey);}
  .lead{stroke:#b9b9b9;stroke-width:.5;fill:none;}
</style>
</head>
<body>
<div class="board">
  <h1 class="board-title">THE PELMAR SLIDE IDEAS ( 5 OPTIONS)</h1>

  <svg class="sprites" aria-hidden="true">
    <defs>
      <linearGradient id="photoTone" x1="0" y1="0" x2="1" y2="1">
        <stop offset="0" stop-color="#4a4c4f"/>
        <stop offset=".55" stop-color="#35373a"/>
        <stop offset="1" stop-color="#222325"/>
      </linearGradient>
      <linearGradient id="fadeBar" x1="0" y1="0" x2="1" y2="0">
        <stop offset="0" stop-color="#d8d8d8"/>
        <stop offset="1" stop-color="#eeeeee"/>
      </linearGradient>
      <clipPath id="pyramidClip"><polygon points="318,48 248,200 388,200"/></clipPath>

      <symbol id="i-list" viewBox="0 0 20 20"><path d="M5 6h10M5 10h10M5 14h10" stroke="currentColor" stroke-width="1.6" fill="none"/></symbol>
      <symbol id="i-doc" viewBox="0 0 20 20"><g stroke="currentColor" stroke-width="1.4" fill="none"><rect x="5" y="3" width="10" height="14" rx="1"/><path d="M7.5 7h5M7.5 10h5M7.5 13h5"/></g></symbol>
      <symbol id="i-frame" viewBox="0 0 20 20"><rect x="3" y="3" width="14" height="14" rx="1" stroke="currentColor" stroke-width="1.6" fill="none"/><rect x="7" y="7" width="6" height="6" fill="currentColor"/></symbol>
      <symbol id="i-check" viewBox="0 0 20 20"><g stroke="currentColor" stroke-width="1.5" fill="none"><rect x="4" y="4" width="12" height="12"/><path d="M7 10l2.5 2.5L13.5 7.5"/></g></symbol>
      <symbol id="i-team" viewBox="0 0 20 20"><g fill="currentColor"><circle cx="6" cy="6" r="1.8"/><circle cx="10" cy="5" r="2"/><circle cx="14" cy="6" r="1.8"/><rect x="4.3" y="8.5" width="3.4" height="7" rx="1.2"/><rect x="8.1" y="7.8" width="3.8" height="8.5" rx="1.3"/><rect x="12.3" y="8.5" width="3.4" height="7" rx="1.2"/></g></symbol>
      <symbol id="i-gear" viewBox="0 0 20 20"><g stroke="currentColor" fill="none"><circle cx="10" cy="10" r="4" stroke-width="1.5"/><circle cx="10" cy="10" r="6.5" stroke-width="1.5"/><circle cx="10" cy="10" r="8" stroke-width="2.4" stroke-dasharray="2.3 2.7"/></g></symbol>

      <g id="hdr">
        <rect width="400" height="225" fill="var(--paper)"/>
        <text class="ttl" x="200" y="24">The Pelmar Difference</text>
        <circle cx="344" cy="18" r="6" fill="var(--grey)"/>
        <text class="brand" x="353" y="21">Pelmar</text>
      </g>

      <g id="para">
        <text><tspan x="0" dy="0">We consider the research and we build client</tspan><tspan x="0" dy="4.2">portfolios with care, seeking the best options</tspan><tspan x="0" dy="4.2">for each investor. Our experience in managing</tspan><tspan x="0" dy="4.2">assets guides every decision we make for you.</tspan><tspan x="0" dy="4.2">Long-term thinking drives our process.</tspan></text>
      </g>
      <g id="para-l">
        <text class="para-l"><tspan x="0" dy="0">Seasoned guidance shaped by decades of careful</tspan><tspan x="0" dy="4">market study and steady, patient client care.</tspan></text>
      </g>

      <g id="cover">
        <rect width="400" height="225" fill="url(#photoTone)" role="img" aria-label="Photograph of classical stone columns in a colonnade"/>
        <rect y="34" width="400" height="38" fill="#1d3256" opacity=".85"/>
        <circle cx="300" cy="53" r="14" fill="#fff"/>
        <text x="319" y="57" font-size="18" fill="#fff">Pelmar</text>
        <text x="320" y="65" font-size="4.5" fill="#fff">CAPITAL WEALTH</text>
        <text x="121" y="180" font-size="13" fill="#fff" text-anchor="middle">The Pelmar Difference</text>
        <text x="121" y="197" font-size="4" fill="#fff" text-anchor="middle">5 SLIDE IDEAS</text>
      </g>
    </defs>
  </svg>

  <!-- Cover -->
  <div class="slide cover-slide" style="left:450px;top:111px">
    <svg viewBox="0 0 400 225"><use href="#cover"/></svg>
  </div>

  <!-- Half donut -->
  <div class="slide" style="left:76px;top:317px">
    <svg viewBox="0 0 400 225"><use href="#hdr"/>
      <g fill="none" stroke-width="32">
        <circle cx="200" cy="145" r="64" stroke="var(--charcoal)" stroke-dasharray="46.9 355.2" transform="rotate(160 200 145)"/>
        <circle cx="200" cy="145" r="64" stroke="var(--navy)" stroke-dasharray="46.9 355.2" transform="rotate(204 200 145)"/>
        <circle cx="200" cy="145" r="64" stroke="var(--charcoal)" stroke-dasharray="46.9 355.2" transform="rotate(248 200 145)"/>
        <circle cx="200" cy="145" r="64" stroke="var(--navy)" stroke-dasharray="46.9 355.2" transform="rotate(292 200 145)"/>
        <circle cx="200" cy="145" r="64" stroke="var(--charcoal)" stroke-dasharray="46.9 355.2" transform="rotate(336 200 145)"/>
        <circle cx="200" cy="145" r="44" stroke="var(--grey)" stroke-width="7" stroke-dasharray="169 300" transform="rotate(160 200 145)"/>
      </g>
      <use href="#i-team" x="129" y="137" width="14" height="14" color="#fff"/>
      <use href="#i-doc" x="148" y="93" width="14" height="14" color="#fff"/>
      <use href="#i-list" x="192" y="74" width="14" height="14" color="#fff"/>
      <use href="#i-frame" x="237" y="91" width="14" height="14" color="#fff"/>
      <use href="#i-check" x="257" y="135" width="14" height="14" color="#fff"/>
      <use href="#i-gear" x="183" y="128" width="34" height="34" color="var(--charcoal)"/>
      <text class="lbl"><tspan x="200" y="50">Proactive Total</tspan><tspan x="200" dy="6">Fee Management</tspan></text>
      <text class="lbl"><tspan x="124" y="66">Sound Operational</tspan><tspan x="124" dy="6">Platform</tspan></text>
      <text class="lbl"><tspan x="278" y="66">Institutional</tspan><tspan x="278" dy="6">Research Process</tspan></text>
      <text class="lbl"><tspan x="100" y="147">Experienced</tspan><tspan x="100" dy="6">Investors</tspan></text>
      <text class="lbl"><tspan x="302" y="147">Transparent</tspan><tspan x="302" dy="6">Communication</tspan></text>
      <circle cx="186" cy="198" r="5" fill="var(--grey)"/><text class="brand" x="194" y="201">Pelmar</text>
    </svg>
  </div>

  <!-- Half donut with text -->
  <div class="slide" style="left:450px;top:317px">
    <svg viewBox="0 0 400 225"><use href="#hdr"/>
      <g fill="none" stroke-width="22">
        <circle cx="200" cy="160" r="44" stroke="var(--charcoal)" stroke-dasharray="32.3 244.2" transform="rotate(160 200 160)"/>
        <circle cx="200" cy="160" r="44" stroke="var(--navy)" stroke-dasharray="32.3 244.2" transform="rotate(204 200 160)"/>
        <circle cx="200" cy="160" r="44" stroke="var(--charcoal)" stroke-dasharray="32.3 244.2" transform="rotate(248 200 160)"/>
        <circle cx="200" cy="160" r="44" stroke="var(--navy)" stroke-dasharray="32.3 244.2" transform="rotate(292 200 160)"/>
        <circle cx="200" cy="160" r="44" stroke="var(--charcoal)" stroke-dasharray="32.3 244.2" transform="rotate(336 200 160)"/>
        <circle cx="200" cy="160" r="30" stroke="var(--grey)" stroke-width="5" stroke-dasharray="115.2 200" transform="rotate(160 200 160)"/>
      </g>
      <use href="#i-team" x="151" y="154" width="10" height="10" color="#fff"/>
      <use href="#i-doc" x="164" y="124" width="10" height="10" color="#fff"/>
      <use href="#i-list" x="194" y="111" width="10" height="10" color="#fff"/>
      <use href="#i-frame" x="225" y="123" width="10" height="10" color="#fff"/>
      <use href="#i-check" x="239" y="153" width="10" height="10" color="#fff"/>
      <use href="#i-gear" x="188" y="148" width="24" height="24" color="var(--charcoal)"/>
      <text class="lbl"><tspan x="200" y="44">Proactive Total</tspan><tspan x="200" dy="5.6">Fee Management</tspan></text>
      <use href="#para" x="200" y="58" class="para" fill="#7a7a7a"/>
      <text class="lbl"><tspan x="62" y="90">Sound Operational</tspan><tspan x="62" dy="5.6">Platform</tspan></text>
      <use href="#para" x="62" y="103" class="para" fill="#7a7a7a"/>
      <text class="lbl"><tspan x="62" y="156">Experienced Investors</tspan></text>
      <use href="#para" x="62" y="163" class="para" fill="#7a7a7a"/>
      <text class="lbl"><tspan x="336" y="92">Institutional</tspan><tspan x="336" dy="5.6">Research Process</tspan></text>
      <use href="#para" x="336" y="105" class="para" fill="#7a7a7a"/>
      <text class="lbl"><tspan x="336" y="157">Transparent Communication</tspan></text>
      <use href="#para" x="336" y="164" class="para" fill="#7a7a7a"/>
      <circle cx="186" cy="200" r="5" fill="var(--grey)"/><text class="brand" x="194" y="203">Pelmar</text>
    </svg>
  </div>

  <!-- Orbit circles -->
  <div class="slide" style="left:824px;top:317px">
    <svg viewBox="0 0 400 225"><use href="#hdr"/>
      <circle cx="200" cy="132" r="22" fill="#fff" stroke="#c9c9c9" stroke-width="1.2"/>
      <circle cx="187" cy="132" r="4" fill="var(--grey)"/><text x="193" y="134.5" font-size="6" fill="var(--grey)">Pelmar</text>
      <circle cx="200" cy="87" r="16" fill="var(--charcoal)"/><use href="#i-list" x="193" y="80" width="14" height="14" color="#fff"/>
      <circle cx="262" cy="122" r="16" fill="var(--blue)"/><use href="#i-frame" x="255" y="115" width="14" height="14" color="#fff"/>
      <circle cx="238" cy="172" r="16" fill="var(--charcoal)"/><use href="#i-check" x="231" y="165" width="14" height="14" color="#fff"/>
      <circle cx="162" cy="172" r="16" fill="var(--charcoal)"/><use href="#i-doc" x="155" y="165" width="14" height="14" color="#fff"/>
      <circle cx="138" cy="122" r="16" fill="var(--navy)"/><use href="#i-team" x="131" y="115" width="14" height="14" color="#fff"/>
      <text class="lbl"><tspan x="200" y="58">Proactive Total</tspan><tspan x="200" dy="6">Fee Management</tspan></text>
      <text class="lbl"><tspan x="98" y="120">Experienced</tspan><tspan x="98" dy="6">Investors</tspan></text>
      <text class="lbl"><tspan x="310" y="120">Institutional</tspan><tspan x="310" dy="6">Research Process</tspan></text>
      <text class="lbl"><tspan x="104" y="178">Sound Operational</tspan><tspan x="104" dy="6">Platform</tspan></text>
      <text class="lbl"><tspan x="290" y="180">Transparent</tspan><tspan x="290" dy="6">Communication</tspan></text>
    </svg>
  </div>

  <!-- Full donut -->
  <div class="slide" style="left:76px;top:528px">
    <svg viewBox="0 0 400 225"><use href="#hdr"/>
      <g fill="none" stroke-width="24">
        <circle cx="200" cy="145" r="50" stroke="var(--blue)" stroke-dasharray="60.2 253.9" transform="rotate(235.5 200 145)"/>
        <circle cx="200" cy="145" r="50" stroke="var(--grey)" stroke-dasharray="60.2 253.9" transform="rotate(307.5 200 145)"/>
        <circle cx="200" cy="145" r="50" stroke="var(--navy)" stroke-dasharray="60.2 253.9" transform="rotate(19.5 200 145)"/>
        <circle cx="200" cy="145" r="50" stroke="var(--charcoal)" stroke-dasharray="60.2 253.9" transform="rotate(91.5 200 145)"/>
        <circle cx="200" cy="145" r="50" stroke="var(--navy)" stroke-dasharray="60.2 253.9" transform="rotate(163.5 200 145)"/>
      </g>
      <circle cx="200" cy="145" r="34" fill="none" stroke="#d4d4d4" stroke-width="4"/>
      <use href="#i-list" x="194" y="89" width="12" height="12" color="#fff"/>
      <use href="#i-frame" x="241.6" y="123.5" width="12" height="12" color="#fff"/>
      <use href="#i-check" x="223.4" y="179.5" width="12" height="12" color="#fff"/>
      <use href="#i-doc" x="164.6" y="179.5" width="12" height="12" color="#fff"/>
      <use href="#i-team" x="146.4" y="123.5" width="12" height="12" color="#fff"/>
      <circle cx="184" cy="145" r="6" fill="var(--grey)"/><text class="brand" x="192" y="148">Pelmar</text>
      <path class="lead" d="M200 70v10M124 112l18 8M276 112l-18 8M108 190l40-10M292 190l-40-10"/>
      <text class="lbl"><tspan x="200" y="56">Proactive Total</tspan><tspan x="200" dy="6">Fee Management</tspan></text>
      <text class="lbl"><tspan x="98" y="102">Experienced</tspan><tspan x="98" dy="6">Investors</tspan></text>
      <text class="lbl"><tspan x="304" y="102">Institutional</tspan><tspan x="304" dy="6">Research Process</tspan></text>
      <text class="lbl"><tspan x="80" y="190">Sound Operational</tspan><tspan x="80" dy="6">Platform</tspan></text>
      <text class="lbl"><tspan x="315" y="190">Transparent</tspan><tspan x="315" dy="6">Communication</tspan></text>
    </svg>
  </div>

  <!-- Full donut with text -->
  <div class="slide" style="left:450px;top:528px">
    <svg viewBox="0 0 400 225"><use href="#hdr"/>
      <g fill="none" stroke-width="18">
        <circle cx="200" cy="160" r="36" stroke="var(--blue)" stroke-dasharray="43.4 182.8" transform="rotate(235.5 200 160)"/>
        <circle cx="200" cy="160" r="36" stroke="var(--grey)" stroke-dasharray="43.4 182.8" transform="rotate(307.5 200 160)"/>
        <circle cx="200" cy="160" r="36" stroke="var(--navy)" stroke-dasharray="43.4 182.8" transform="rotate(19.5 200 160)"/>
        <circle cx="200" cy="160" r="36" stroke="var(--charcoal)" stroke-dasharray="43.4 182.8" transform="rotate(91.5 200 160)"/>
        <circle cx="200" cy="160" r="36" stroke="var(--navy)" stroke-dasharray="43.4 182.8" transform="rotate(163.5 200 160)"/>
      </g>
      <circle cx="200" cy="160" r="24" fill="none" stroke="#d4d4d4" stroke-width="3"/>
      <use href="#i-list" x="195.5" y="119.5" width="9" height="9" color="#fff"/>
      <use href="#i-frame" x="229.7" y="144.4" width="9" height="9" color="#fff"/>
      <use href="#i-check" x="216.7" y="184.6" width="9" height="9" color="#fff"/>
      <use href="#i-doc" x="174.3" y="184.6" width="9" height="9" color="#fff"/>
      <use href="#i-team" x="161.3" y="144.4" width="9" height="9" color="#fff"/>
      <circle cx="187" cy="160" r="5" fill="var(--grey)"/><text x="194" y="162.5" font-size="6.5" fill="var(--grey)">Pelmar</text>
      <text class="lbl"><tspan x="200" y="44">Proactive Total Fee Management</tspan></text>
      <use href="#para" x="200" y="51" class="para" fill="#7a7a7a"/>
      <text class="lbl"><tspan x="98" y="104">Experienced Investors</tspan></text>
      <use href="#para" x="98" y="111" class="para" fill="#7a7a7a"/>
      <text class="lbl"><tspan x="98" y="163">Sound Operational Platform</tspan></text>
      <use href="#para" x="98" y="170" class="para" fill="#7a7a7a"/>
      <text class="lbl"><tspan x="306" y="104">Institutional  Research Process</tspan></text>
      <use href="#para" x="306" y="111" class="para" fill="#7a7a7a"/>
      <text class="lbl"><tspan x="306" y="163">Transparent Communication</tspan></text>
      <use href="#para" x="306" y="170" class="para" fill="#7a7a7a"/>
    </svg>
  </div>

  <!-- Pie with pentagon -->
  <div class="slide" style="left:824px;top:528px">
    <svg viewBox="0 0 400 225"><use href="#hdr"/>
      <g fill="none" stroke-width="58">
        <circle cx="200" cy="148" r="29" stroke="var(--charcoal)" stroke-dasharray="36.44 145.8" transform="rotate(234 200 148)"/>
        <circle cx="200" cy="148" r="29" stroke="var(--blue)" stroke-dasharray="36.44 145.8" transform="rotate(306 200 148)"/>
        <circle cx="200" cy="148" r="29" stroke="var(--grey)" stroke-dasharray="36.44 145.8" transform="rotate(18 200 148)"/>
        <circle cx="200" cy="148" r="29" stroke="var(--navy)" stroke-dasharray="36.44 145.8" transform="rotate(90 200 148)"/>
        <circle cx="200" cy="148" r="29" stroke="var(--teal)" stroke-dasharray="36.44 145.8" transform="rotate(162 200 148)"/>
      </g>
      <polygon points="180,120.5 220,120.5 232.3,158.5 200,182 167.7,158.5" fill="#fff"/>
      <circle cx="189" cy="150" r="3.5" fill="var(--grey)"/><text x="194" y="152" font-size="5.5" fill="var(--grey)">Pelmar</text>
      <use href="#i-list" x="194" y="96" width="12" height="12" color="#fff"/>
      <use href="#i-frame" x="237.7" y="127.8" width="12" height="12" color="#fff"/>
      <use href="#i-check" x="221" y="179.2" width="12" height="12" color="#fff"/>
      <use href="#i-doc" x="167" y="179.2" width="12" height="12" color="#fff"/>
      <use href="#i-team" x="150.3" y="127.8" width="12" height="12" color="#fff"/>
      <text class="lbl"><tspan x="200" y="54">Proactive Total</tspan><tspan x="200" dy="6">Fee Management</tspan></text>
      <text class="lbl"><tspan x="106" y="120">Experienced</tspan><tspan x="106" dy="6">Investors</tspan></text>
      <text class="lbl"><tspan x="314" y="120">Institutional</tspan><tspan x="314" dy="6">Research Process</tspan></text>
      <text class="lbl"><tspan x="112" y="179">Sound Operational</tspan><tspan x="112" dy="6">Platform</tspan></text>
      <text class="lbl"><tspan x="308" y="179">Transparent</tspan><tspan x="308" dy="6">Communication</tspan></text>
    </svg>
  </div>

  <!-- Linked rings -->
  <div class="slide" style="left:76px;top:743px">
    <svg viewBox="0 0 400 225"><use href="#hdr"/>
      <g fill="none" stroke-width="10">
        <circle cx="90" cy="142" r="28" stroke="var(--ring)"/>
        <circle cx="145" cy="142" r="28" stroke="var(--ring)"/>
        <circle cx="200" cy="142" r="28" stroke="var(--ring)"/>
        <circle cx="255" cy="142" r="28" stroke="var(--ring)"/>
        <circle cx="310" cy="142" r="28" stroke="var(--ring)"/>
        <path d="M62 142A28 28 0 0 1 118 142" stroke="var(--navy)"/>
        <path d="M117 142A28 28 0 0 0 173 142" stroke="var(--pink)"/>
        <path d="M172 142A28 28 0 0 1 228 142" stroke="var(--charcoal)"/>
        <path d="M227 142A28 28 0 0 0 283 142" stroke="var(--purple)"/>
        <path d="M282 142A28 28 0 0 1 338 142" stroke="var(--teal)"/>
      </g>
      <use href="#i-team" x="83" y="135" width="14" height="14" color="var(--charcoal)"/>
      <use href="#i-list" x="138" y="135" width="14" height="14" color="var(--charcoal)"/>
      <use href="#i-doc" x="193" y="135" width="14" height="14" color="var(--charcoal)"/>
      <use href="#i-frame" x="248" y="135" width="14" height="14" color="var(--charcoal)"/>
      <use href="#i-check" x="303" y="135" width="14" height="14" color="var(--charcoal)"/>
      <path class="lead" d="M145 101v6M255 101v6M90 180v6M200 180v6M310 180v6"/>
      <text class="lbl"><tspan x="145" y="89">Proactive Total</tspan><tspan x="145" dy="6">Fee Management</tspan></text>
      <text class="lbl"><tspan x="255" y="89">Institutional Research</tspan><tspan x="255" dy="6">Process</tspan></text>
      <text class="lbl"><tspan x="90" y="194">Experienced</tspan><tspan x="90" dy="6">Investors</tspan></text>
      <text class="lbl"><tspan x="200" y="194">Sound Operational</tspan><tspan x="200" dy="6">Platform</tspan></text>
      <text class="lbl"><tspan x="310" y="194">Transparent</tspan><tspan x="310" dy="6">Communication</tspan></text>
    </svg>
  </div>

  <!-- Linked rings with text -->
  <div class="slide" style="left:450px;top:743px">
    <svg viewBox="0 0 400 225"><use href="#hdr"/>
      <g fill="none" stroke-width="8">
        <circle cx="104" cy="148" r="20" stroke="var(--ring)"/>
        <circle cx="152" cy="148" r="20" stroke="var(--ring)"/>
        <circle cx="200" cy="148" r="20" stroke="var(--ring)"/>
        <circle cx="248" cy="148" r="20" stroke="var(--ring)"/>
        <circle cx="296" cy="148" r="20" stroke="var(--ring)"/>
        <path d="M84 148A20 20 0 0 1 124 148" stroke="var(--navy)"/>
        <path d="M132 148A20 20 0 0 0 172 148" stroke="var(--pink)"/>
        <path d="M180 148A20 20 0 0 1 220 148" stroke="var(--charcoal)"/>
        <path d="M228 148A20 20 0 0 0 268 148" stroke="var(--purple)"/>
        <path d="M276 148A20 20 0 0 1 316 148" stroke="var(--teal)"/>
      </g>
      <use href="#i-team" x="98" y="142" width="12" height="12" color="var(--charcoal)"/>
      <use href="#i-list" x="146" y="142" width="12" height="12" color="var(--charcoal)"/>
      <use href="#i-doc" x="194" y="142" width="12" height="12" color="var(--charcoal)"/>
      <use href="#i-frame" x="242" y="142" width="12" height="12" color="var(--charcoal)"/>
      <use href="#i-check" x="290" y="142" width="12" height="12" color="var(--charcoal)"/>
      <text class="lbl"><tspan x="144" y="57">Proactive Total Fee Management</tspan></text>
      <use href="#para" x="144" y="64" class="para" fill="#7a7a7a"/>
      <text class="lbl"><tspan x="260" y="57">Institutional  Research Process</tspan></text>
      <use href="#para" x="260" y="64" class="para" fill="#7a7a7a"/>
      <text class="lbl"><tspan x="66" y="178">Experienced Investors</tspan></text>
      <use href="#para" x="66" y="185" class="para" fill="#7a7a7a"/>
      <text class="lbl"><tspan x="200" y="178">Sound Operational Platform</tspan></text>
      <use href="#para" x="200" y="185" class="para" fill="#7a7a7a"/>
      <text class="lbl"><tspan x="330" y="178">Transparent Communication</tspan></text>
      <use href="#para" x="330" y="185" class="para" fill="#7a7a7a"/>
    </svg>
  </div>

  <!-- Panels -->
  <div class="slide" style="left:824px;top:743px">
    <svg viewBox="0 0 400 225"><use href="#hdr"/>
      <rect x="5" y="63" width="75" height="125" fill="#737576"/>
      <rect x="84" y="63" width="75" height="125" fill="var(--charcoal)"/>
      <rect x="163" y="63" width="75" height="125" fill="#737576"/>
      <rect x="242" y="63" width="75" height="125" fill="var(--charcoal)"/>
      <rect x="321" y="63" width="75" height="125" fill="#737576"/>
      <text class="lbl-w"><tspan x="42.5" y="76">Experienced</tspan><tspan x="42.5" dy="5.6">Investors</tspan></text>
      <text class="lbl-w"><tspan x="121.5" y="76">Proactive Total</tspan><tspan x="121.5" dy="5.6">Fee Management</tspan></text>
      <text class="lbl-w"><tspan x="200.5" y="76">Sound Operational</tspan><tspan x="200.5" dy="5.6">Platform</tspan></text>
      <text class="lbl-w"><tspan x="279.5" y="76">Institutional</tspan><tspan x="279.5" dy="5.6">Research Process</tspan></text>
      <text class="lbl-w"><tspan x="358.5" y="76">Transparent</tspan><tspan x="358.5" dy="5.6">Communication</tspan></text>
      <use href="#i-team" x="35.5" y="93" width="14" height="14" color="#fff"/>
      <use href="#i-list" x="114.5" y="93" width="14" height="14" color="#fff"/>
      <use href="#i-doc" x="193.5" y="93" width="14" height="14" color="#fff"/>
      <use href="#i-frame" x="272.5" y="93" width="14" height="14" color="#fff"/>
      <use href="#i-check" x="351.5" y="93" width="14" height="14" color="#fff"/>
      <use href="#para" class="para" fill="#e4e4e4" transform="translate(42.5 122) scale(.8)"/>
      <use href="#para" class="para" fill="#e4e4e4" transform="translate(121.5 122) scale(.8)"/>
      <use href="#para" class="para" fill="#e4e4e4" transform="translate(200.5 122) scale(.8)"/>
      <use href="#para" class="para" fill="#e4e4e4" transform="translate(279.5 122) scale(.8)"/>
      <use href="#para" class="para" fill="#e4e4e4" transform="translate(358.5 122) scale(.8)"/>
    </svg>
  </div>

  <!-- Pyramid -->
  <div class="slide" style="left:76px;top:949px">
    <svg viewBox="0 0 400 225"><use href="#hdr"/>
      <rect x="70" y="52" width="236" height="22" fill="url(#fadeBar)"/>
      <rect x="55" y="82" width="251" height="22" fill="url(#fadeBar)"/>
      <rect x="40" y="112" width="266" height="22" fill="url(#fadeBar)"/>
      <rect x="25" y="142" width="281" height="22" fill="url(#fadeBar)"/>
      <rect x="10" y="172" width="296" height="22" fill="url(#fadeBar)"/>
      <polygon points="78,52 100,52 92,74 70,74" fill="#3b6cb3"/>
      <polygon points="63,82 85,82 77,104 55,104" fill="var(--charcoal)"/>
      <polygon points="48,112 70,112 62,134 40,134" fill="var(--navy)"/>
      <polygon points="33,142 55,142 47,164 25,164" fill="var(--purple)"/>
      <polygon points="18,172 40,172 32,194 10,194" fill="var(--grey)"/>
      <text class="lbl-s" x="104" y="60">Experienced Investors</text><use href="#para-l" x="104" y="65"/>
      <text class="lbl-s" x="89" y="90">Proactive Total Fee Management</text><use href="#para-l" x="89" y="95"/>
      <text class="lbl-s" x="74" y="120">Sound Operational Platform</text><use href="#para-l" x="74" y="125"/>
      <text class="lbl-s" x="59" y="150">Institutional Research Process</text><use href="#para-l" x="59" y="155"/>
      <text class="lbl-s" x="44" y="180">Transparent Communication</text><use href="#para-l" x="44" y="185"/>
      <g clip-path="url(#pyramidClip)">
        <rect x="240" y="48" width="160" height="30" fill="#3b6cb3"/>
        <rect x="240" y="78" width="160" height="30" fill="var(--charcoal)"/>
        <rect x="240" y="108" width="160" height="30" fill="var(--navy)"/>
        <rect x="240" y="138" width="160" height="30" fill="var(--purple)"/>
        <rect x="240" y="168" width="160" height="32" fill="var(--grey)"/>
      </g>
      <use href="#i-team" x="313" y="62" width="10" height="10" color="#fff"/>
      <use href="#i-list" x="313" y="88" width="10" height="10" color="#fff"/>
      <use href="#i-doc" x="313" y="118" width="10" height="10" color="#fff"/>
      <use href="#i-frame" x="313" y="148" width="10" height="10" color="#fff"/>
      <use href="#i-check" x="313" y="178" width="10" height="10" color="#fff"/>
    </svg>
  </div>

  <!-- Overlapping circles -->
  <div class="slide" style="left:450px;top:949px">
    <svg viewBox="0 0 400 225"><use href="#hdr"/>
      <circle cx="88" cy="115" r="25" fill="var(--navy)"/>
      <circle cx="144" cy="115" r="25" fill="var(--grey)"/>
      <circle cx="200" cy="115" r="25" fill="var(--charcoal)"/>
      <circle cx="256" cy="115" r="25" fill="var(--blue)"/>
      <circle cx="312" cy="115" r="25" fill="var(--teal)"/>
      <use href="#i-team" x="81" y="108" width="14" height="14" color="#fff"/>
      <use href="#i-list" x="137" y="108" width="14" height="14" color="#fff"/>
      <use href="#i-doc" x="193" y="108" width="14" height="14" color="#fff"/>
      <use href="#i-frame" x="249" y="108" width="14" height="14" color="#fff"/>
      <use href="#i-check" x="305" y="108" width="14" height="14" color="#fff"/>
      <path class="lead" d="M144 72v15M256 72v15M88 143v10M200 143v10M312 143v10"/>
      <text class="lbl"><tspan x="144" y="57">Proactive Total</tspan><tspan x="144" dy="6">Fee Management</tspan></text>
      <text class="lbl"><tspan x="256" y="57">Institutional Research</tspan><tspan x="256" dy="6">Process</tspan></text>
      <text class="lbl"><tspan x="88" y="172">Experienced</tspan><tspan x="88" dy="6">Investors</tspan></text>
      <text class="lbl"><tspan x="200" y="172">Sound</tspan><tspan x="200" dy="6">Operational</tspan><tspan x="200" dy="6">Platform</tspan></text>
      <text class="lbl"><tspan x="312" y="172">Transparent</tspan><tspan x="312" dy="6">Communication</tspan></text>
    </svg>
  </div>

  <!-- Closing -->
  <div class="slide cover-slide" style="left:824px;top:949px">
    <svg viewBox="0 0 400 225"><use href="#cover"/></svg>
  </div>
</div>
</body>
</html>
```